Real Estate Business Cards

Looking for a clean, sharp and professional look for our Real Estate investment Fund that invests in Multi Family Apartment buildings.

Target Market(s)

Real Estate Fund

Industry/Entity Type

Real Estate

Contact Information for Business Card

Company Description: Real Estate Investment Fund
Company Name: KRV Holdings
Name: Marcus Tovell
Cell: (917) 482-0957
Email: marcus@krvholdings-example.com
Website: www.krvholdings-example.com
Address: 148, 7th Street, Brooklyn NY 11217

Colors

Designer to choose colors to be used in the design.

Requirements
Nice to have
• Colors to match logo

```html
<!DOCTYPE html>
<html lang="en">
<head>
<meta charset="utf-8">
<title>KRV Holdings – Business Card</title>
<link href="https://fonts.googleapis.com/css2?family=Arimo:wght@400;700&display=swap" rel="stylesheet">
<style>
  :root {
    --stage: #1c1c1c;
    --card: #2f2f2f;
    --card-front: #2b2b2b;
    --accent: #1a75b3;
    --ink: #ffffff;
    --ink-soft: #e8e8e8;
  }
  * { box-sizing: border-box; margin: 0; padding: 0; }
  html, body {
    width: 1200px; height: 900px; overflow: hidden;
    background: var(--stage);
    font-family: "Arimo", Arial, sans-serif;
  }
  .stage {
    width: 1200px; height: 900px;
    display: flex; flex-direction: column; align-items: center; justify-content: center;
    gap: 40px;
  }
  .card {
    position: relative;
    width: 630px; height: 360px;
    background: var(--card);
    box-shadow: 0 10px 30px rgba(0,0,0,.55);
    overflow: hidden;
  }
  .card::after {
    content: ""; position: absolute; left: 0; right: 0; bottom: 0;
    height: 14px; background: var(--accent);
  }
  .card--front {
    background: var(--card-front);
    display: flex; align-items: center; justify-content: center;
  }
  .brand {
    display: flex; align-items: center; gap: 12px;
    color: var(--ink);
    font-weight: 400;
    letter-spacing: 3px;
    text-transform: uppercase;
  }
  .brand__square { width: 14px; height: 14px; background: var(--ink); }
  .card--front .brand { font-size: 26px; margin-bottom: 14px; }

  .card--back .brand {
    position: absolute; left: 40px; top: 160px;
    font-size: 24px; color: var(--accent);
  }
  .card--back .brand__square { background: var(--accent); }
  .divider {
    position: absolute; left: 300px; top: 90px;
    width: 2px; height: 180px; background: var(--accent);
  }
  .contact {
    position: absolute; left: 325px; top: 88px;
    color: var(--ink-soft);
    font-size: 15px; line-height: 1.3;
  }
  .contact__name {
    color: var(--accent); font-weight: 700; font-size: 22px;
    text-transform: uppercase; line-height: 1.1;
  }
  .contact__role { color: var(--ink); font-weight: 700; font-size: 16px; margin-bottom: 14px; }
  .contact__address { margin-bottom: 12px; }
  .contact__line { display: flex; align-items: center; gap: 10px; margin-bottom: 6px; }
  .contact__line svg { width: 14px; height: 14px; flex: none; }
  .contact__web-domain { color: var(--accent); }
</style>
</head>
<body>
<main class="stage">
  <section class="card card--front" aria-label="Business card front">
    <div class="brand"><span class="brand__square"></span>KRV Holdings</div>
  </section>

  <section class="card card--back" aria-label="Business card back">
    <div class="brand"><span class="brand__square"></span>KRV Holdings</div>
    <div class="divider"></div>
    <div class="contact">
      <div class="contact__name">Marcus Tovell</div>
      <div class="contact__role">CEO</div>
      <div class="contact__address">148, 7th Street,<br>Brooklyn NY 11217</div>
      <div class="contact__line">
        <svg viewBox="0 0 16 16" aria-hidden="true"><path d="M3 1.5l3 .5 1 3-1.8 1.3a9 9 0 0 0 4.5 4.5L11 9l3 1 .5 3-2 1.5C7 14 2 9 1.5 3.5z" fill="none" stroke="#1a75b3" stroke-width="1.4"/></svg>
        (917) 482-0957
      </div>
      <div class="contact__line">
        <svg viewBox="0 0 16 16" aria-hidden="true"><rect x="1.5" y="3.5" width="13" height="9" fill="none" stroke="#1a75b3" stroke-width="1.4"/><path d="M1.5 3.5L8 9l6.5-5.5" fill="none" stroke="#1a75b3" stroke-width="1.4"/></svg>
        marcus@krvholdings-example.com
      </div>
      <div class="contact__line">
        <svg viewBox="0 0 16 16" aria-hidden="true"><circle cx="8" cy="8" r="6.5" fill="none" stroke="#1a75b3" stroke-width="1.4"/><path d="M1.5 8h13M8 1.5c-3 3.5-3 9.5 0 13M8 1.5c3 3.5 3 9.5 0 13" fill="none" stroke="#1a75b3" stroke-width="1.2"/></svg>
        <span>www.<span class="contact__web-domain">krvholdings-example</span>.com</span>
      </div>
    </div>
  </section>
</main>
</body>
</html>
```